Business Card Design

Attached is my current Business card I do not like it but I must save the logo portion of it. Don't like the color or the lettering am looking for more architectural look in grays or taupe with the green more of a charturese color and the blue a charcoal color on a textured paper that looks more like something high-end that would appeal to an architect or a designer. We make concrete decorative items such as concrete fireplaces, sinks, tops and more.

Target Market(s)

Architects designers of Commercial and Residential - artistic features

Industry/Entity Type

Architect

Contact Information for Business Card

Maren T. Oakes President and Marketing Director
602-418-5563
email maren@velmorstoneworks.example
Showroom "Tavlin Design Center" 4126 W Harlow Row Scottsdale AZ
Fax: 602-871-2046

Font styles to use
Sans Serif

Requirements
Must have
• Architectural
Natural and earthy colors with a touch of color in the existing attached

```html
<!DOCTYPE html>
<html lang="en">
<head>
<meta charset="utf-8">
<title>Velmor Stoneworks — Business Card</title>
<link rel="stylesheet" href="https://fonts.googleapis.com/css2?family=Orbitron:wght@500&family=Montserrat:wght@400;600&display=swap">
<style>
  :root {
    --paper-taupe: #d9d3c5;
    --paper-shade: #cbc4b3;
    --stone-gray: #9d998f;
    --ink-charcoal: #3a3d41;
    --accent-chartreuse: #a9c930;
    --ink-soft: #5b5d5f;
  }
  html, body {
    margin: 0;
    padding: 0;
    overflow: hidden;
    background: var(--paper-taupe);
  }
  .card {
    position: relative;
    width: 1200px;
    height: 702px;
    overflow: hidden;
    background-color: var(--paper-taupe);
    background-image:
      radial-gradient(circle at 20% 30%, rgba(255,255,255,0.35), transparent 55%),
      radial-gradient(circle at 80% 70%, rgba(120,110,90,0.18), transparent 60%),
      radial-gradient(rgba(90,85,75,0.12) 1px, transparent 1.4px);
    background-size: 100% 100%, 100% 100%, 7px 7px;
    font-family: "Montserrat", sans-serif;
    color: var(--ink-charcoal);
  }
  .card__decor {
    position: absolute;
    inset: 0;
    width: 1200px;
    height: 702px;
  }
  .brand {
    position: absolute;
    left: 238px;
    top: 262px;
    display: flex;
    align-items: center;
    gap: 22px;
  }
  .brand__square {
    width: 34px;
    height: 34px;
    background: var(--accent-chartreuse);
  }
  .brand__name {
    margin: 0;
    font-family: "Orbitron", sans-serif;
    font-size: 50px;
    font-weight: 500;
    letter-spacing: 6px;
    color: var(--ink-charcoal);
    text-transform: uppercase;
    white-space: nowrap;
  }
  .brand__rule {
    position: absolute;
    left: 330px;
    top: 358px;
    width: 610px;
    height: 2px;
    background: var(--accent-chartreuse);
  }
  .contact {
    position: absolute;
    top: 386px;
    left: 330px;
    width: 610px;
    display: grid;
    grid-template-columns: 310px 280px;
    column-gap: 20px;
    font-size: 16px;
    line-height: 27px;
  }
  .contact p { margin: 0; white-space: nowrap; }
  .contact__name {
    font-weight: 600;
    font-size: 19px;
    letter-spacing: 0.5px;
  }
  .contact__title,
  .contact__label { color: var(--ink-soft); }
  .contact__title { font-size: 14px; }
  .contact__showroom { font-weight: 600; }
</style>
</head>
<body>
  <main class="card">
    <svg class="card__decor" viewBox="0 0 1200 702" xmlns="http://www.w3.org/2000/svg">
      <defs>
        <linearGradient id="fragmentTones" x1="0" y1="0" x2="1" y2="1">
          <stop offset="0" stop-color="#a9c930"/>
          <stop offset="0.5" stop-color="#55585b"/>
          <stop offset="1" stop-color="#9d998f"/>
        </linearGradient>
      </defs>
      <path class="decor-left" role="img"
            aria-label="Scattered angular fragments in chartreuse, charcoal and stone gray along the left edge"
            fill="url(#fragmentTones)" opacity="0.45"
            d="M0 0 H310 L230 120 L170 260 L200 420 L300 560 L470 702 H0 Z"/>
      <path class="decor-right" role="img"
            aria-label="Scattered angular fragments in chartreuse, charcoal and stone gray in the lower right corner"
            fill="url(#fragmentTones)" opacity="0.45"
            d="M1200 460 V702 H880 L960 560 L1100 500 Z"/>
    </svg>

    <header class="brand">
      <span class="brand__square" aria-hidden="true"></span>
      <h1 class="brand__name">Velmor Stoneworks</h1>
    </header>
    <div class="brand__rule" aria-hidden="true"></div>

    <section class="contact">
      <div class="contact__person">
        <p class="contact__name">Maren T. Oakes</p>
        <p class="contact__title">President and Marketing Director</p>
        <p class="contact__phone">602-418-5563</p>
        <p class="contact__email">maren@velmorstoneworks.example</p>
      </div>
      <div class="contact__showroom-block">
        <p class="contact__showroom">Showroom: Tavlin Design Center</p>
        <p class="contact__address">4126 W Harlow Row</p>
        <p class="contact__city">Scottsdale AZ</p>
        <p class="contact__fax"><span class="contact__label">Fax:</span> 602-871-2046</p>
      </div>
    </section>
  </main>
</body>
</html>
```